Travel Blogger Business Card for roamquill.net

I need a two-sided business card for a travel blogging website. The card should be both professional and fun at the same time. This is for the website www.roamquill.net

I don't necessarily think that the current logo on the website needs to be used on the business card but it can be. I am very flexible with ideas

Target Market(s)

Travel agencies that will be met at a conference.

Industry/Entity Type

Travel

Contact Information for Business Card

Company Name: Roam Quill.net
Name: Bertrand Olesky
Voice: +1-(345)-402-7731
Address: Coral Reach Shore, Grand Cayman, Cayman Islands
Email: ceo@roamquill.net

Colors
0592cd
0355a3
3176b5
33a6d7
85cae6
85acd3

Requirements
Must have
• Website address and name should be bigger than address, phone number, and email.

```html
<!DOCTYPE html>
<html lang="en">
<head>
<meta charset="utf-8">
<title>Roam Quill.net – Business Card</title>
<link rel="stylesheet" href="https://fonts.googleapis.com/css2?family=Montserrat:wght@200;300;400;700&family=Open+Sans:wght@400;700&display=swap">
<style>
  :root {
    --page-bg: #ffffff;
    --card-frame: #1d63d9;
    --card-back: #1f56df;
    --ink-dark: #1b3fa8;
    --ink-light: #ffffff;
    --sky-top: #bfeaf7;
    --sky-low: #8fd9f0;
    --sea-far: #3cb5d6;
    --sea-near: #7fdde8;
    --sand: #d9f2ef;
  }
  * { margin: 0; padding: 0; box-sizing: border-box; }
  html, body {
    width: 1200px;
    height: 919px;
    overflow: hidden;
    background: var(--page-bg);
  }
  .canvas {
    position: relative;
    width: 1200px;
    height: 919px;
  }
  .card {
    position: absolute;
    width: 700px;
    height: 400px;
    overflow: hidden;
  }

  /* Front */
  .card-front {
    left: 80px;
    top: 50px;
    border: 6px solid var(--card-frame);
  }
  .front-photo {
    position: absolute;
    inset: 0;
    background: linear-gradient(180deg,
      var(--sky-top) 0%,
      var(--sky-low) 40%,
      var(--sea-far) 46%,
      var(--sea-near) 70%,
      var(--sand) 100%);
  }
  .front-brand {
    position: absolute;
    top: 26px;
    right: 30px;
    text-align: right;
    color: var(--ink-light);
  }
  .brand-name {
    font-family: "Montserrat", sans-serif;
    font-weight: 300;
    font-size: 40px;
    line-height: 1.1;
  }
  .person-name {
    font-family: "Open Sans", sans-serif;
    font-weight: 700;
    font-size: 19px;
    margin-top: 10px;
  }
  .website {
    font-family: "Open Sans", sans-serif;
    font-weight: 400;
    font-size: 19px;
    line-height: 1.2;
  }
  .front-contact {
    position: absolute;
    right: 30px;
    bottom: 22px;
    text-align: right;
    color: var(--ink-dark);
    font-family: "Open Sans", sans-serif;
    font-size: 17px;
    line-height: 1.45;
  }

  /* Back */
  .card-back {
    left: 420px;
    top: 470px;
    background: var(--card-back);
  }
  .back-url {
    position: absolute;
    left: 120px;
    top: 90px;
    width: 470px;
    height: 78px;
    border: 1.5px solid rgba(255, 255, 255, 0.85);
    border-radius: 8px;
    display: flex;
    align-items: center;
    justify-content: center;
    color: var(--ink-light);
    font-family: "Montserrat", sans-serif;
    font-weight: 200;
    font-size: 42px;
    letter-spacing: 0.5px;
  }
  .back-brand {
    position: absolute;
    left: 0;
    right: 0;
    bottom: 70px;
    display: flex;
    align-items: center;
    justify-content: center;
    gap: 10px;
    color: var(--ink-light);
    font-family: "Montserrat", sans-serif;
    font-weight: 700;
    font-size: 20px;
    letter-spacing: 0.5px;
  }
  .brand-dot {
    width: 22px;
    height: 22px;
    border-radius: 50%;
    background: var(--ink-light);
  }
</style>
</head>
<body>
<main class="canvas">

  <section class="card card-front">
    <div class="front-photo" role="img" aria-label="Beach photo: white parasol and two wooden deck chairs standing in shallow turquoise water under a pale sky"></div>
    <div class="front-brand">
      <p class="brand-name">Roam Quill.net</p>
      <p class="person-name">Bertrand Olesky</p>
      <p class="website">www.roamquill.net</p>
    </div>
    <div class="front-contact">
      <p class="phone">Tel: +1-(345)-402-7731</p>
      <p class="email">ceo@roamquill.net</p>
      <p class="address">#Coral Reach Shore, Grand Cayman, Cayman Islands</p>
    </div>
  </section>

  <section class="card card-back">
    <div class="back-url">www.roamquill.net</div>
    <div class="back-brand">
      <span class="brand-dot"></span>
      <span class="brand-wordmark">ROAM QUILL</span>
    </div>
  </section>

</main>
</body>
</html>
```